Family Ranch with a hobby vineyard needs 2 wine labels for our first harvest

Design 2 wine labels (front and back) with the Brindor Ranch logo.
Label 1:
Sauvignon Blanc
Alc. 12.5% by Vol.
Palos Verdes Peninsula - add as the region
Year 2022
Label 2:
Cabernet Sauvignon
Alc. 13.5% by Vol.
Year 2022
For the back label design:
GOVERNMENT WARNING: (1) According to the Surgeon General, women
should not drink alcoholic beverages during pregnancy because of the risk of
birth defects. (2) Consumption of alcoholic beverages impairs your ability to
drive a car or operate machinery, and may cause health problems.
Contains Sulfates.
750ML
I just received the bottles and have attached a picture.
Look and feel
Each slider illustrates characteristics of the customer's brand and the style your logo design should communicate.

```html
<!DOCTYPE html>
<html lang="en">
<head>
<meta charset="UTF-8">
<title>Brindor Ranch – Sauvignon Blanc 2022 Label</title>
<link href="https://fonts.googleapis.com/css2?family=Pinyon+Script&family=Libre+Baskerville:wght@400&display=swap" rel="stylesheet">
<style>
  :root {
    --backdrop: #f6f6f5;
    --paper: #ecebe7;
    --wine-red: #6d1a26;
    --ink: #4a4a4a;
    --ink-soft: #6a6a6a;
    --sketch-light: #e6e5e1;
    --sketch-mid: #c9c9c6;
  }
  * { box-sizing: border-box; margin: 0; padding: 0; }
  html, body {
    width: 1200px;
    height: 1200px;
    overflow: hidden;
    background: var(--backdrop);
  }
  .canvas {
    position: relative;
    width: 1200px;
    height: 1200px;
  }
  .front-label {
    position: absolute;
    left: 225px;
    top: 50px;
    width: 750px;
    height: 1100px;
    background: var(--paper);
    box-shadow: 0 2px 14px rgba(0,0,0,0.08);
  }
  .label-frame {
    position: absolute;
    inset: 0;
    width: 100%;
    height: 100%;
  }
  .brand {
    position: absolute;
    top: 150px;
    left: 0;
    right: 0;
    display: flex;
    flex-direction: column;
    align-items: center;
    gap: 22px;
  }
  .brand-dot {
    width: 80px;
    height: 80px;
    border-radius: 50%;
    background: var(--ink);
  }
  .brand-name {
    font-family: "Libre Baskerville", Georgia, serif;
    font-size: 34px;
    letter-spacing: 4px;
    text-transform: uppercase;
    color: var(--ink);
  }
  .varietal {
    position: absolute;
    top: 418px;
    left: 0;
    right: 0;
    text-align: center;
    font-family: "Pinyon Script", cursive;
    font-size: 76px;
    color: var(--wine-red);
    line-height: 1;
  }
  .region {
    position: absolute;
    top: 520px;
    left: 0;
    right: 0;
    text-align: center;
    font-family: "Libre Baskerville", Georgia, serif;
    font-size: 23px;
    letter-spacing: 2px;
    color: var(--ink);
  }
  .coastal-scene {
    position: absolute;
    top: 600px;
    left: 55px;
    width: 640px;
    height: 340px;
    background: radial-gradient(ellipse at 55% 60%, var(--sketch-mid) 0%, var(--sketch-light) 55%, var(--paper) 80%);
  }
  .vintage {
    position: absolute;
    top: 942px;
    left: 0;
    right: 0;
    text-align: center;
    font-family: "Libre Baskerville", Georgia, serif;
    font-size: 38px;
    letter-spacing: 2px;
    color: var(--wine-red);
  }
  .volume {
    position: absolute;
    top: 1018px;
    left: 0;
    right: 0;
    text-align: center;
    font-family: "Libre Baskerville", Georgia, serif;
    font-size: 23px;
    letter-spacing: 1.5px;
    color: var(--ink-soft);
  }
</style>
</head>
<body>
<div class="canvas">
  <section class="front-label">
    <svg class="label-frame" viewBox="0 0 750 1100" aria-hidden="true">
      <rect x="10" y="10" width="730" height="1080" fill="none" stroke="var(--wine-red)" stroke-width="3"/>
      <rect x="21" y="21" width="708" height="1058" fill="none" stroke="var(--wine-red)" stroke-width="1.5"/>
    </svg>

    <div class="brand">
      <div class="brand-dot"></div>
      <div class="brand-name">Brindor Ranch</div>
    </div>

    <h1 class="varietal">Sauvignon Blanc</h1>
    <p class="region">PALOS VERDES PENINSULA</p>

    <div class="coastal-scene" role="img" aria-label="Pencil sketch of a lighthouse on a rocky coastal bluff with pine trees and the sea beyond"></div>

    <p class="vintage">2022</p>
    <p class="volume">ALC. 12.5% BY VOL &bull; 750ML</p>
  </section>
</div>
</body>
</html>
```